Business Card Design needed for logo design project

We need a business card design for a construction parts business.

We would like our main company logo on the front of the card and have our other company website logo on the rear of the card.

Both logos will be attached.

Front of card
Logo is KRV
Can we also have the wording "Construction Equipment Parts Specialists"
Main details to include:

Address:
Telephone:
Mobile:
Email:
Website:

Rear of card.

Logo is gearlodgehub.com.au (we would like this logo taking up the most of the rear)
Also we want under gearlodgehub.com.au the following wording "Parts Sourced For You From Across The Globe"
Updates

Please see new update for our design

Target Market(s)

Construction Industry.
Earthmoving Equipment owners.

Industry/Entity Type

Construction

Font styles to use
Sans Serif

Requirements
Must have
• Easy to read.
Clean and smart.
Should not have
• Should not have any colours other than the colours of our logos.

```html
<!DOCTYPE html>
<html lang="en">
<head>
<meta charset="utf-8">
<title>KRV Business Card – Front and Rear</title>
<link rel="stylesheet" href="https://fonts.googleapis.com/css2?family=Oswald:wght@400;500;600;700&display=swap">
<style>
  :root {
    --navy: #1f3447;
    --teal: #2a8aa0;
    --teal-faint: #dcebf0;
    --paper: #ffffff;
    --backdrop: #e9ecee;
  }
  * { margin: 0; padding: 0; box-sizing: border-box; }
  html, body {
    width: 1200px; height: 1000px; overflow: hidden;
    background: var(--backdrop);
    font-family: "Oswald", "Arial Narrow", sans-serif;
    color: var(--navy);
  }
  .sheet {
    width: 1200px; height: 1000px;
    display: flex; flex-direction: column;
    align-items: center; justify-content: center; gap: 60px;
  }
  .card {
    position: relative;
    width: 700px; height: 400px;
    background: var(--paper);
    box-shadow: 0 6px 20px rgba(0,0,0,.12);
    overflow: hidden;
  }

  /* Front */
  .front .accent-bar {
    position: absolute; left: 0; top: 46px;
    width: 210px; height: 22px; background: var(--teal);
  }
  .front .brand {
    position: absolute; left: 52px; top: 92px;
    display: flex; align-items: center; gap: 14px;
  }
  .front .brand-name {
    font-weight: 700; font-size: 84px; line-height: 1;
    letter-spacing: 2px; color: var(--navy);
  }
  .front .brand-dot {
    width: 38px; height: 38px; border-radius: 50%; background: var(--teal);
  }
  .front .tagline-band {
    position: absolute; left: 52px; right: 0; top: 210px;
    height: 34px; background: var(--teal);
    display: flex; align-items: center; padding-left: 18px;
    color: var(--paper); font-weight: 500; font-size: 19px;
    letter-spacing: 1.5px; text-transform: uppercase;
  }
  .front .contacts {
    position: absolute; right: 44px; top: 44px;
    list-style: none; display: flex; flex-direction: column; gap: 8px;
  }
  .contact-item {
    display: flex; align-items: center; gap: 10px;
    font-size: 17px; font-weight: 500; letter-spacing: 1px;
    text-transform: uppercase; color: var(--navy);
  }
  .icon { width: 20px; height: 20px; flex: none; }
  .front .address {
    position: absolute; left: 70px; bottom: 36px;
    display: flex; gap: 10px; align-items: flex-start;
  }
  .front .address-lines {
    font-style: normal; font-size: 17px; font-weight: 500;
    letter-spacing: 1px; line-height: 1.35; text-transform: uppercase;
  }

  /* Rear */
  .rear .emblem-field {
    position: absolute; left: 40px; top: -70px;
    width: 300px; height: 300px; border-radius: 50%;
    background: var(--teal-faint);
  }
  .rear .wordmark {
    position: absolute; left: 56px; top: 150px;
    display: flex; align-items: center; gap: 16px;
  }
  .rear .wordmark-name {
    font-weight: 700; font-size: 58px; line-height: 1;
    letter-spacing: 1px; color: var(--navy); text-transform: uppercase;
  }
  .rear .wordmark-dot {
    width: 52px; height: 52px; border-radius: 50%; background: var(--teal);
  }
  .rear .tagline {
    position: absolute; left: 58px; top: 238px;
    font-weight: 500; font-size: 19px; letter-spacing: 2.4px;
    color: var(--teal); text-transform: uppercase;
  }
</style>
</head>
<body>
<main class="sheet">

  <section class="card front" aria-label="Card front">
    <div class="accent-bar"></div>
    <div class="brand">
      <span class="brand-name">KRV</span>
      <span class="brand-dot"></span>
    </div>
    <div class="tagline-band">Construction Equipment Parts Specialists</div>

    <ul class="contacts">
      <li class="contact-item">
        <svg class="icon" viewBox="0 0 20 20" aria-label="Telephone"><rect width="20" height="20" rx="4" fill="#2a8aa0"/><path d="M6 5l2 0 1 3-1.5 1a6 6 0 0 0 3.5 3.5L12 11l3 1 0 2c-5 1-10-4-9-9z" fill="#fff"/></svg>
        0123 4567 890
      </li>
      <li class="contact-item">
        <svg class="icon" viewBox="0 0 20 20" aria-label="Mobile"><rect width="20" height="20" rx="4" fill="#2a8aa0"/><rect x="7" y="4" width="6" height="12" rx="1" fill="#fff"/><rect x="8" y="5.5" width="4" height="7" fill="#2a8aa0"/></svg>
        0123 4567 890
      </li>
      <li class="contact-item">
        <svg class="icon" viewBox="0 0 20 20" aria-label="Email"><rect width="20" height="20" rx="4" fill="#2a8aa0"/><rect x="4" y="6" width="12" height="8" fill="#fff"/><path d="M4 6l6 5 6-5" fill="none" stroke="#2a8aa0" stroke-width="1.2"/></svg>
        your@email.com
      </li>
      <li class="contact-item">
        <svg class="icon" viewBox="0 0 20 20" aria-label="Website"><rect width="20" height="20" rx="4" fill="#2a8aa0"/><circle cx="10" cy="10" r="5.5" fill="none" stroke="#fff" stroke-width="1.4"/><path d="M4.5 10h11M10 4.5c-3 3.5-3 7.5 0 11M10 4.5c3 3.5 3 7.5 0 11" fill="none" stroke="#fff" stroke-width="1"/></svg>
        gearlodgehub.com.au
      </li>
    </ul>

    <div class="address">
      <svg class="icon" viewBox="0 0 20 20" aria-label="Address"><rect width="20" height="20" rx="4" fill="#2a8aa0"/><path d="M10 3.5a4.5 4.5 0 0 0-4.5 4.5c0 3.5 4.5 8.5 4.5 8.5s4.5-5 4.5-8.5A4.5 4.5 0 0 0 10 3.5z" fill="#fff"/><circle cx="10" cy="8" r="1.7" fill="#2a8aa0"/></svg>
      <address class="address-lines">
        Gearlodgehub<br>
        Address Line 1<br>
        Line 2<br>
        Your Address Line 3
      </address>
    </div>
  </section>

  <section class="card rear" aria-label="Card rear">
    <div class="emblem-field" role="img" aria-label="Faint large brand emblem in a circle"></div>
    <div class="wordmark">
      <span class="wordmark-name">gearlodgehub.com.au</span>
      <span class="wordmark-dot"></span>
    </div>
    <p class="tagline">Parts Sourced For You From Across The Globe</p>
  </section>

</main>
</body>
</html>
```